Concierge Dental / Medical Supply Ordering Business - Sleek, Efficient, Professional, Elite

www.brimleyandfoxcare.example - example website.

We are a concierge supply ordering business for medical and dental that provide DSO price savings on supplies while maintaining business autonomy and independence.

We want a very simple website that looks very professional says what we do and gives a very simple method to contact us & sign up as above.

Target Market(s)

Independent Dental and Medical Practices

Industry/Entity Type

Dental and Medical - healthcare

Coding

Coded - Design and coding required

Number of Pages Required

3 page

Font styles to use
Sans Serif

Colors
0054AA
0677BA
7BADD7
CADEEF
E8F1F8

Requirements
Must have
• Simple contact page, sleek efficient design, uncomplicated.
Nice to have
• Sign up page vs just a contact page.
Should not have
• Lots of pages, hard to navigate,

```html
<!DOCTYPE html>
<html lang="en">
<head>
<meta charset="utf-8">
<title>Brimley and Fox Care</title>
<link rel="stylesheet" href="https://fonts.googleapis.com/css2?family=Montserrat:wght@500;600;700&family=Open+Sans:wght@400;600;700&display=swap">
<style>
:root{
  --blue-deep:#0054AA;
  --blue:#0677BA;
  --blue-mid:#7BADD7;
  --blue-soft:#CADEEF;
  --blue-pale:#E8F1F8;
  --white:#ffffff;
  --text:#34475c;
  --footer:#0b2a4f;
  --footer-field:#1d416b;
  --video-a:#2f4f73;
  --video-b:#1c3553;
}
*{margin:0;padding:0;box-sizing:border-box}
html,body{width:1200px;height:4692px;overflow:hidden}
body{position:relative;background:var(--white);font-family:"Open Sans",sans-serif;color:var(--text)}
.abs{position:absolute}
.head{font-family:"Montserrat",sans-serif}
h1,h2{font-family:"Montserrat",sans-serif;color:var(--blue-deep);font-weight:700;letter-spacing:.3px}
.label{font-size:8px;font-weight:700;letter-spacing:.5px;color:var(--blue-deep);text-transform:uppercase}
.para{font-size:11.5px;line-height:18px;color:var(--text)}
.btn{position:absolute;background:var(--blue);color:#fff;font-size:10px;font-weight:700;display:flex;align-items:center;justify-content:center;text-transform:uppercase;letter-spacing:.3px}
.accent{position:absolute;width:34px;height:2px;background:var(--blue)}
.photo{position:absolute;background:linear-gradient(135deg,var(--blue-soft),var(--blue-mid))}
.band{position:absolute;left:0;width:1200px}
.nav{position:absolute;top:32px;left:332px;display:flex;font-size:13px;color:var(--blue-deep)}
.nav span{display:block;margin-right:66px}
.card{position:absolute;top:1546px;width:318px;height:295px;background:#fff}
.card .photo{left:0;top:0;width:100%;height:191px}
.card p{position:absolute;top:233px;width:100%;text-align:center;font-family:"Montserrat",sans-serif;font-weight:500;font-size:19px;color:var(--blue-deep)}
.why{position:absolute;background:#fff;width:255px;height:158px}
.why p{position:absolute;left:30px;top:92px;font-family:"Montserrat",sans-serif;font-weight:500;font-size:15px;line-height:21px;color:var(--blue-deep)}
.why .num{position:absolute;right:28px;top:36px;font-family:"Montserrat",sans-serif;font-weight:500;font-size:68px;color:var(--blue-soft)}
.why svg{position:absolute;left:30px;top:26px}
.field{position:absolute;background:#fff;font-size:10px;color:#5a6b7d;padding:20px 22px}
.foot-label{font-size:9px;color:var(--blue-mid);text-transform:uppercase;letter-spacing:.4px}
.foot-val{font-family:"Montserrat",sans-serif;font-weight:500;font-size:15px;color:#fff}
</style>
</head>
<body>

<!-- hero -->
<div class="abs" style="left:0;top:0;width:1012px;height:657px;background:var(--blue-pale)"></div>
<nav class="nav"><span>HOME</span><span>ABOUT US</span><span>SERVICES</span><span>CONTACT US</span></nav>
<h1 class="abs" style="left:140px;top:204px;font-size:46px;line-height:60px">Supply Ordering<br>Done Right,<br>Every Time</h1>
<p class="abs para" style="left:140px;top:398px;width:340px">Lorem ipsum dolor sit amet, consectetur adipiscing elit, sed do eiusmod tempor incididunt</p>
<div class="btn" style="left:140px;top:461px;width:137px;height:53px">Learn more</div>
<div class="photo" role="img" aria-label="Two businessmen reviewing an order on a tablet" style="left:586px;top:67px;width:578px;height:519px"></div>
<div class="abs" style="left:1047px;top:612px;width:118px;display:flex;align-items:center;justify-content:space-between;font-size:9px;color:var(--blue-deep)">
  <svg width="26" height="8"><path d="M26 4H2M6 1L2 4L6 7" stroke="#0054AA" fill="none"/></svg>1 OF 3<svg width="26" height="8"><path d="M0 4H24M20 1L24 4L20 7" stroke="#0054AA" fill="none"/></svg>
</div>

<!-- about -->
<div class="photo" role="img" aria-label="Two doctors talking in a clinic" style="left:138px;top:761px;width:365px;height:385px"></div>
<div class="abs" style="left:217px;top:1063px;width:364px;height:148px;background:var(--blue-deep)">
  <svg class="abs" style="left:58px;top:56px" width="38" height="38" viewBox="0 0 24 24"><path d="M6.6 10.8a15 15 0 0 0 6.6 6.6l2.2-2.2c.3-.3.7-.4 1-.2 1.1.4 2.3.6 3.6.6.6 0 1 .4 1 1V20c0 .6-.4 1-1 1A17 17 0 0 1 3 4c0-.6.4-1 1-1h3.5c.6 0 1 .4 1 1 0 1.3.2 2.5.6 3.6.1.3 0 .7-.2 1z" fill="none" stroke="#fff" stroke-width="1.2"/></svg>
  <p class="abs" style="left:115px;top:46px;font-size:13px;color:var(--blue-soft)">For Calls:</p>
  <p class="abs head" style="left:115px;top:68px;font-size:21px;font-weight:700;color:#fff">0 800-555-40-18</p>
</div>
<p class="abs label" style="left:661px;top:765px">About us</p>
<h2 class="abs" style="left:661px;top:797px;font-size:38px;line-height:58px">Supply Solutions for<br>Medical Success</h2>
<div class="accent" style="left:661px;top:925px"></div>
<p class="abs para" style="left:661px;top:955px;width:320px">Lorem ipsum dolor sit amet, consectetur adipiscing elit, sed do eiusmod tempor incididunt ut labore et dolor e magna aliqua. e magna aliqua. e magna</p>
<p class="abs para" style="left:661px;top:1028px;width:320px">Lorem ipsum dolor sit amet, consectetur adipiscing elit, sed do eiusmod tempor incididunt ut labore et dolor e magna aliqua. e magna aliqua. e magna Lorem ipsum dolor sit amet, consectetur adipiscing elit, sed do eiusmod tempor incididunt ut labore et dolor</p>
<div class="btn" style="left:661px;top:1147px;width:133px;height:51px">Learn more</div>

<!-- services -->
<div class="band" style="top:1280px;height:727px;background:var(--blue-pale)"></div>
<p class="abs label" style="left:86px;top:1375px">Our services</p>
<h2 class="abs" style="left:86px;top:1405px;font-size:42px">Services We Provide</h2>
<div class="accent" style="left:86px;top:1490px"></div>
<div class="card" style="left:84px"><div class="photo" role="img" aria-label="Colleagues reviewing orders on a tablet"></div><p>Order Fulfillment</p></div>
<div class="card" style="left:432px"><div class="photo" role="img" aria-label="Two women comparing prices on a laptop"></div><p>Price Savings</p></div>
<div class="card" style="left:778px"><div class="photo" role="img" aria-label="Team meeting around a table"></div><p>Timely Delivery</p></div>
<div class="btn" style="left:519px;top:1883px;width:131px;height:51px">Learn more</div>

<!-- video -->
<div class="band" role="img" aria-label="Team of professionals talking in an office" style="top:2009px;height:453px;background:linear-gradient(135deg,var(--video-a),var(--video-b) 60%,var(--video-a))"></div>
<div class="abs" style="left:514px;top:2127px;width:160px;height:160px;border:1.5px solid #fff;border-radius:50%"></div>
<svg class="abs" style="left:585px;top:2186px" width="16" height="18"><path d="M2 2L14 9L2 16Z" fill="none" stroke="#fff" stroke-width="1.5"/></svg>
<p class="abs" style="left:514px;top:2215px;width:160px;text-align:center;color:#fff;font-size:14px;font-weight:600">Play Video</p>
<p class="abs head" style="left:0;top:2322px;width:1200px;text-align:center;color:#fff;font-size:44px;font-weight:500">Explanation Video</p>

<!-- why choose -->
<div class="band" style="top:2462px;height:506px;background:var(--blue-pale)"></div>
<p class="abs label" style="left:102px;top:2568px">Why choose us</p>
<h2 class="abs" style="left:104px;top:2600px;font-size:38px;line-height:56px">Your Supply<br>Partner for Success</h2>
<div class="accent" style="left:102px;top:2728px"></div>
<p class="abs para" style="left:102px;top:2752px;width:320px">Lorem ipsum dolor sit amet, consectetur adipiscing elit, sed do eiusmod tempor incididunt ut labore et dolor e magna aliqua. e magna aliqua. e magna</p>
<div class="btn" style="left:102px;top:2837px;width:133px;height:53px">Learn more</div>
<div class="why" style="left:577px;top:2568px"><svg width="44" height="40" viewBox="0 0 44 40"><path d="M6 34A18 18 0 1 1 38 34" fill="none" stroke="#0054AA" stroke-width="2"/><path d="M22 26L22 12M16 16l3 4M28 16l-3 4" stroke="#0054AA" stroke-width="2"/></svg><p>Quality<br>Assurance</p><span class="num">1</span></div>
<div class="why" style="left:839px;top:2568px"><svg width="44" height="44" viewBox="0 0 44 44"><circle cx="22" cy="22" r="14" fill="none" stroke="#0054AA" stroke-width="2"/><circle cx="22" cy="22" r="5" fill="none" stroke="#0054AA" stroke-width="2"/><path d="M22 2v10M22 32v10M2 22h10M32 22h10" stroke="#0054AA" stroke-width="2"/></svg><p>Client-Centric<br>Approach</p><span class="num">2</span></div>
<div class="why" style="left:577px;top:2733px"><svg width="44" height="40" viewBox="0 0 44 40"><path d="M8 36h28M14 30h16M20 30l8-22M24 6l6 2" fill="none" stroke="#0054AA" stroke-width="2"/><circle cx="14" cy="20" r="6" fill="none" stroke="#0054AA" stroke-width="2"/></svg><p>Research<br>Capabilities</p><span class="num">3</span></div>
<div class="why" style="left:839px;top:2733px"><svg width="44" height="40" viewBox="0 0 44 40"><path d="M22 4L38 16L32 36H12L6 16Z" fill="none" stroke="#0054AA" stroke-width="2"/></svg><p>Delivery<br>Excellence</p><span class="num">4</span></div>

<!-- pathway -->
<div class="band" style="top:2968px;height:1333px;background:var(--blue-pale)"></div>
<div class="band" role="img" aria-label="Team meeting with a video call on a wall screen" style="top:2968px;height:492px;background:linear-gradient(135deg,var(--video-a),var(--video-b) 55%,var(--video-a))"></div>
<h2 class="abs" style="left:151px;top:3076px;font-size:50px;line-height:64px;color:#fff">Your Pathway to<br>Supply Ordering Success</h2>
<p class="abs para" style="left:151px;top:3240px;width:330px;color:var(--blue-pale)">Lorem ipsum dolor sit amet, consectetur adipiscing elit, sed do eiusmod tempor incididunt ut labore et dolor</p>
<div class="btn" style="left:151px;top:3307px;width:168px;height:49px;font-size:9px">Go to services page</div>
<div class="abs" style="left:379px;top:3369px;width:661px;height:269px;background:#fff">
  <p class="abs" style="left:76px;top:62px;width:410px;font-size:15px;line-height:26px;color:var(--text)">Lorem ipsum dolor sit amet, consectetur ad ipiscing elit, sed do eiusmod tempor incididunt ut labore et dolore magna aliqua. Ut enim ad minim veniam, quis nostrud exercitation ullamco laboris nisi ut aliquip ex ea commodo consequat. Duis aute irure dolor in reprehenderit</p>
  <p class="abs head" style="left:510px;top:50px;font-size:140px;line-height:140px;font-weight:700;color:var(--blue-deep)">”</p>
</div>

<!-- contact -->
<div class="photo" role="img" aria-label="Smiling man holding a tablet" style="left:151px;top:3724px;width:359px;height:422px"></div>
<div class="abs" style="left:239px;top:4039px;width:271px;height:107px;background:var(--blue-deep)">
  <svg class="abs" style="left:34px;top:36px" width="40" height="34" viewBox="0 0 40 34"><rect x="2" y="6" width="36" height="26" fill="none" stroke="#CADEEF" stroke-width="2"/><path d="M2 6L20 20L38 6" fill="none" stroke="#CADEEF" stroke-width="2"/></svg>
  <p class="abs" style="left:88px;top:34px;font-size:8px;color:var(--blue-soft);text-transform:uppercase">Need to contact us?</p>
  <p class="abs head" style="left:88px;top:52px;font-size:17px;font-weight:500;color:#fff">Email Us</p>
</div>
<p class="abs label" style="left:609px;top:3690px">Contact with us</p>
<h2 class="abs" style="left:609px;top:3722px;font-size:42px;line-height:58px">Any Questions?<br>Let’s Talk!</h2>
<div class="accent" style="left:609px;top:3851px"></div>
<div class="field" style="left:606px;top:3899px;width:215px;height:51px">My name is</div>
<div class="field" style="left:825px;top:3899px;width:215px;height:51px">My e-mail</div>
<div class="field" style="left:606px;top:3957px;width:434px;height:49px">I am interested in</div>
<div class="field" style="left:606px;top:4013px;width:434px;height:133px">My message is</div>
<div class="btn" style="left:896px;top:4165px;width:144px;height:51px;font-size:9px">Send a message</div>

<!-- footer -->
<footer class="band" style="top:4301px;height:391px;background:var(--footer)">
  <p class="abs foot-label" style="left:104px;top:102px">Visit office:</p>
  <p class="abs foot-val" style="left:104px;top:122px">48 Harbor Lane, Suite 7</p>
  <div class="accent" style="left:104px;top:152px;background:var(--blue-mid)"></div>
  <p class="abs foot-label" style="left:104px;top:175px">Write email:</p>
  <p class="abs foot-val" style="left:104px;top:196px;font-size:14px">hello@brimleyandfoxcare.example</p>
  <div class="accent" style="left:104px;top:228px;background:var(--blue-mid)"></div>
  <p class="abs foot-label" style="left:104px;top:251px">Make a call:</p>
  <p class="abs foot-val" style="left:104px;top:271px">0 (800)-555-27-90</p>

  <div class="abs" style="left:560px;top:160px;width:50px;height:50px;border:2px solid var(--blue-mid)"></div>
  <p class="abs head" style="left:440px;top:238px;width:290px;text-align:center;font-size:16px;font-weight:700;color:#fff">Brimley and Fox Care</p>
  <p class="abs" style="left:440px;top:276px;width:290px;text-align:center;font-size:11px;color:var(--blue-mid)">www.brimleyandfoxcare.example</p>

  <p class="abs foot-label" style="left:869px;top:128px">Subscribe to our news</p>
  <p class="abs head" style="left:869px;top:148px;width:250px;font-size:14px;font-weight:500;line-height:22px;color:#fff">Always Get Our Latest News &amp; Events Newsletter!</p>
  <div class="abs" style="left:869px;top:226px;width:178px;height:38px;background:var(--footer-field);font-size:10px;color:var(--blue-soft);padding:12px 18px">your email</div>
  <div class="abs" style="left:1056px;top:226px;width:44px;height:38px;background:var(--blue)"><svg style="position:absolute;left:16px;top:12px" width="12" height="14"><path d="M3 2L9 7L3 12" fill="none" stroke="#fff" stroke-width="2"/></svg></div>
</footer>
</body>
</html>
```